Design a Flyer all white party ATL

This is going to an all white party(meaning that all the guess will wear all white clothes). This party will be an African - American Party.
I want the MPD logo small of the flyer
I will be sending a KELVOZ design later (you can design a sample one... i might like and use it)
The Info:
Saturday Sept. 1 2018 at The Copper Lantern ATL
4830 Merriwick Rd. Lithonia, GA 30412
KELVOZ is take over the Copper Lantern Labor Day Weekend
The Last All White Party For 2018
Tickets $10 in advance $20 at the door
Get your ticket now

```html
<!DOCTYPE html>
<html lang="en">
<head>
<meta charset="utf-8">
<title>White Party Flyer</title>
<link href="https://fonts.googleapis.com/css2?family=Big+Shoulders+Display:wght@300&family=Oswald:wght@400;500;600&display=swap" rel="stylesheet">
<style>
  :root {
    --page-bg: #e6e6e8;
    --flyer-light: #f7f7f9;
    --flyer-mid: #dcdde3;
    --flyer-cool: #c9cbd6;
    --ink: #2a2a2e;
    --gold: #b8903f;
    --red: #d0201f;
    --title-white: #ffffff;
    --rule: #b59a62;
  }
  * { margin: 0; padding: 0; box-sizing: border-box; }
  html, body {
    width: 1040px; height: 1200px; overflow: hidden;
    background: var(--page-bg);
  }
  .flyer {
    position: absolute; left: 70px; top: 18px;
    width: 900px; height: 1164px; overflow: hidden;
    background: var(--flyer-light);
    font-family: "Oswald", sans-serif;
    text-align: center;
  }
  .flyer__backdrop {
    position: absolute; inset: 0;
    background:
      radial-gradient(ellipse 60% 28% at 50% 58%, rgba(185,188,206,0.55), transparent 70%),
      radial-gradient(circle at 78% 20%, rgba(255,255,255,0.95), transparent 30%),
      radial-gradient(circle at 14% 30%, rgba(205,207,216,0.6), transparent 22%),
      radial-gradient(circle at 90% 88%, rgba(210,212,220,0.55), transparent 20%),
      linear-gradient(180deg, var(--flyer-light) 0%, var(--flyer-mid) 45%, var(--flyer-cool) 60%, var(--flyer-light) 80%, #ededf0 100%);
  }
  .brand {
    position: absolute; top: 40px; left: 0; right: 0;
  }
  .brand__name {
    font-weight: 600; font-size: 54px; line-height: 1; color: var(--ink);
    letter-spacing: 2px;
  }
  .brand__tagline {
    font-weight: 600; font-size: 17px; color: var(--ink); margin-top: 2px;
  }
  .title {
    position: absolute; left: 0; right: 0; top: 160px;
    font-family: "Big Shoulders Display", sans-serif; font-weight: 300;
    color: var(--title-white);
    text-shadow: 4px 6px 6px rgba(60,62,80,0.35), 0 0 2px rgba(120,122,140,0.5);
    line-height: 0.9;
  }
  .title__line { display: block; font-size: 300px; letter-spacing: 4px; }
  .title__line--second { font-size: 270px; }
  .date {
    position: absolute; left: 0; right: 0; top: 770px;
    font-weight: 600; font-size: 42px; color: var(--title-white);
    text-shadow: 2px 2px 3px rgba(20,20,30,0.75);
    letter-spacing: 0.5px;
  }
  .date sup { font-size: 26px; vertical-align: 14px; }
  .venue {
    position: absolute; left: 0; right: 0; top: 893px;
    font-weight: 500; font-size: 32px; color: var(--gold);
  }
  .details {
    position: absolute; left: 166px; width: 568px; top: 940px;
    border-top: 2px solid var(--rule); border-bottom: 2px solid var(--rule);
    padding: 10px 0 10px;
  }
  .details__address { font-size: 26px; color: var(--ink); line-height: 1.2; }
  .details__takeover { font-size: 21px; color: var(--gold); line-height: 1.3; }
  .cta {
    position: absolute; left: 0; right: 0; top: 1060px;
    font-size: 22px; color: var(--gold); font-weight: 500;
  }
  .tickets {
    position: absolute; left: 0; right: 0; top: 1088px;
    font-size: 30px; color: var(--ink); font-weight: 500;
  }
  .tickets__price { color: var(--red); }
</style>
</head>
<body>
  <main class="flyer">
    <div class="flyer__backdrop" role="img" aria-label="Soft white and pale silver party backdrop with glossy balloons, roses and light flares"></div>

    <header class="brand">
      <div class="brand__name">MPD</div>
      <div class="brand__tagline">Mellow People Dance</div>
    </header>

    <h1 class="title">
      <span class="title__line">WHITE</span>
      <span class="title__line title__line--second">PARTY</span>
    </h1>

    <p class="date">SATURDAY 1<sup>ST</sup> SEPTEMBER 2018</p>

    <p class="venue">AT THE COPPER LANTERN ATL</p>

    <div class="details">
      <p class="details__address">4830 MERRIWICK RD. LITHONIA, GA 30412</p>
      <p class="details__takeover">KELVOZ IS TAKE OVER THE COPPER LANTERN LABOR DAY WEEKEND</p>
    </div>

    <p class="cta">GET YOUR TICKET NOW</p>
    <p class="tickets">TICKETS <span class="tickets__price">$10</span> IN ADVANCE <span class="tickets__price">$20</span> AT THE DOOR</p>
  </main>
</body>
</html>
```